Ironfinch Steakhouse

We are changing our restaurant from a casual upmarket dining restaurant, to an upmarket steakhouse. The restaurant is located at Ironfinch Lodge, Silver Pike Alpine Resort, BC, Canada.

The A - frame Signs are 3 feet wide by 5 foot high.
Must also work as a poster size.

Target Market(s)

25 to 65's skiers, families, affluent home owners.

Industry/Entity Type

Restaurant

Colors

Designer to choose colors to be used in the design.

Requirements
Must have
• A big, juicy, flame grilled steak image.
• Located at Ironfinch lodge.
Nice to have
• Must be bold and enticing, need to convince the tired skiers that they just have to have an awesome steak for dinner.
• Should be simple, straight to the point.
• People drinking, dining, having a great dining experience.
Should not have
• bright colors

```html
<!DOCTYPE html>
<html lang="en">
<head>
<meta charset="utf-8">
<title>Ironfinch Steakhouse Poster</title>
<link href="https://fonts.googleapis.com/css2?family=Anton&family=Alfa+Slab+One&family=Cinzel:wght@400&family=Roboto+Slab:wght@700&family=Crimson+Text:ital,wght@1,600&display=swap" rel="stylesheet">
<style>
  :root {
    --ember-dark: #1c1009;
    --ember-mid: #3b1d10;
    --maroon: #5c1d16;
    --gold: #e8a920;
    --smoke: #2a2a24;
    --white: #f7f2ea;
  }
  * { margin: 0; padding: 0; box-sizing: border-box; }
  html, body { width: 797px; height: 1200px; overflow: hidden; background: #d9d6d0; }
  .poster {
    position: relative; width: 797px; height: 1200px; overflow: hidden;
    background: linear-gradient(180deg, var(--ember-mid) 0%, var(--ember-dark) 100%);
  }
  .interior-photo {
    position: absolute; left: 0; top: 0; width: 450px; height: 440px;
    background: radial-gradient(ellipse at 40% 30%, #c9923f 0%, #7a4a22 45%, #2e1a10 100%);
  }
  .interior-photo::after {
    content: ""; position: absolute; inset: 46px 28px 30px 40px;
    background: linear-gradient(160deg, #b07a3c 0%, #5d3a20 55%, #2a1a10 100%);
    box-shadow: 0 0 0 3px rgba(247,220,160,.35);
  }
  .brand-column {
    position: absolute; left: 450px; top: 0; width: 347px; height: 440px;
    background: linear-gradient(180deg, #2c2a22 0%, #3a2c1c 60%, #5a3416 100%);
  }
  .brand-mark {
    position: absolute; left: 0; right: 0; top: 70px; text-align: center;
    font-family: 'Cinzel', serif; font-weight: 400; color: var(--white);
    font-size: 34px; line-height: 1.15; letter-spacing: 1px;
  }
  .brand-mark .dot {
    display: block; width: 46px; height: 46px; margin: 0 auto 18px;
    border-radius: 50%; background: var(--white);
  }
  .gold-band {
    position: absolute; left: 0; width: 797px; height: 16px; background: var(--gold);
  }
  .gold-band.top { top: 462px; }
  .gold-band.bottom { top: 830px; }
  .headline-block {
    position: absolute; left: 0; top: 478px; width: 797px; height: 352px;
    background: linear-gradient(90deg, var(--maroon) 0%, var(--maroon) 45%, #1a120e 45%, #1a120e 100%);
  }
  .headline {
    position: absolute; left: 0; right: 0; top: 22px; text-align: center;
    color: var(--white); font-family: 'Anton', sans-serif; text-transform: uppercase; font-weight: 400;
  }
  .headline .lead { display: block; font-size: 64px; line-height: 1; letter-spacing: 1px; }
  .headline .hero {
    display: block; font-family: 'Alfa Slab One', serif; text-transform: none; font-weight: 400;
    color: var(--gold); font-size: 150px; line-height: 1;
  }
  .headline .close { display: block; font-size: 78px; line-height: 1; letter-spacing: 1px; }
  .steak-photo {
    position: absolute; left: 0; top: 846px; width: 797px; height: 354px;
    background: radial-gradient(ellipse at 20% 70%, #c8661e 0%, #5a2410 35%, #1e100a 75%);
  }
  .guests-photo {
    position: absolute; right: 18px; top: 870px; width: 290px; height: 290px;
    background: linear-gradient(140deg, #7a3a2a 0%, #4a2030 50%, #2a2a4a 100%);
    box-shadow: 0 0 0 2px rgba(232,169,32,.35);
  }
  .location {
    position: absolute; left: 40px; top: 950px; width: 430px; text-align: center; color: var(--white);
  }
  .location .title { font-family: 'Roboto Slab', serif; font-weight: 700; font-size: 42px; line-height: 1.08; }
  .location .sub { font-family: 'Crimson Text', serif; font-style: italic; font-weight: 600; font-size: 24px; margin-top: 14px; }
</style>
</head>
<body>
  <main class="poster">
    <div class="interior-photo" role="img" aria-label="Guests dining in a warmly lit restaurant interior"></div>
    <div class="brand-column">
      <div class="brand-mark"><span class="dot"></span>Ironfinch<br>Steakhouse</div>
    </div>

    <div class="gold-band top"></div>
    <section class="headline-block">
      <h1 class="headline">
        <span class="lead">Just have to have an</span>
        <span class="hero">awesome</span>
        <span class="close">Steak for dinner</span>
      </h1>
    </section>
    <div class="gold-band bottom"></div>

    <div class="steak-photo" role="img" aria-label="Big juicy steak sizzling over flame grill"></div>
    <div class="guests-photo" role="img" aria-label="Couple toasting with glasses of red wine"></div>

    <div class="location">
      <p class="title">Located at<br>Ironfinch Lodge</p>
      <p class="sub">Silver Pike Alpine Resort, BC</p>
    </div>
  </main>
</body>
</html>
```